Dunvarra windows & Home Improvements

We are a family run business with over 35 years expertise. Myself and father run it
We supply and install a rated windows and all types of doors and
Verandel composite doors .
We also specialise in renovating houses and adding extensions on to houses .
Are biggest selling point is the quality of the products we provide . we give 15 year guarantee on all windows and doors

I need flyers to distribute at shows and also to put through letterboxes
they can be a6 or a5 which ever works best . I have attached some images and our logo. Images don't have to be used

I have a show on the 29th march so need them fairly fast. Been designing them myself on this but they just don't look right

```html
<!DOCTYPE html>
<html lang="en">
<head>
<meta charset="utf-8">
<title>Dunvarra Windows &amp; Home Improvements – Flyer</title>
<link href="https://fonts.googleapis.com/css2?family=Roboto+Condensed:ital,wght@0,300;0,400;0,700;1,400&display=swap" rel="stylesheet">
<style>
  :root {
    --brand-blue: #1f5ba7;
    --brand-navy: #1b4d8f;
    --ink-dark: #1a1a1a;
    --ink-grey: #7a7a7a;
    --white: #ffffff;
    --photo-sky: #c9d6e2;
    --photo-grass: #6f8d4a;
  }
  * { margin: 0; padding: 0; box-sizing: border-box; }
  html, body { width: 846px; height: 1200px; overflow: hidden; background: var(--white); }
  .flyer {
    position: relative; width: 846px; height: 1200px; overflow: hidden;
    font-family: "Roboto Condensed", "Arial Narrow", sans-serif; color: var(--brand-navy);
    background: linear-gradient(180deg, #f4f6f8 0%, #ffffff 30%);
  }
  .abs { position: absolute; }

  .intro { left: 43px; top: 40px; }
  .intro-lead { font-size: 25px; font-weight: 400; line-height: 34px; }
  .intro-title { font-size: 32px; font-weight: 700; line-height: 38px; letter-spacing: .3px; margin-top: 2px; }
  .intro-tail { font-size: 25px; line-height: 34px; margin-top: 2px; }

  .worker-photo { left: 560px; top: 0; width: 286px; height: 330px;
    background: linear-gradient(160deg, #dfe5ea 0%, #8fa9cc 55%, #3b3f46 100%); }

  .band { left: 0; top: 0; }

  .photo { left: 26px; width: 322px; border: 2px solid var(--white); }
  .photo-sunroom { top: 260px; height: 278px;
    background: linear-gradient(180deg, var(--photo-sky) 0%, #e6e6e2 55%, var(--photo-grass) 100%); }
  .photo-extension { top: 522px; height: 278px;
    background: linear-gradient(180deg, #e3e6ea 0%, #8a8078 40%, #2c2f33 70%, #a59d94 100%); }

  .badge { left: 504px; top: 184px; width: 152px; height: 152px; border-radius: 50%;
    background: var(--white); border: 4px solid var(--brand-blue);
    display: flex; flex-direction: column; align-items: center; justify-content: center; text-align: center; }
  .badge-years { font-size: 27px; line-height: 30px; }
  .badge-years strong { font-size: 44px; font-weight: 700; }
  .badge-label { font-size: 27px; line-height: 32px; }

  .services { left: 392px; top: 350px; width: 440px; list-style: none; color: var(--white); }
  .service { position: relative; padding-left: 29px; font-size: 24px; font-weight: 700; line-height: 29px; margin-bottom: 20px; }
  .service::before { content: ""; position: absolute; left: 0; top: 8px; width: 0; height: 0;
    border-left: 18px solid transparent; border-bottom: 16px solid var(--white); }
  .service-note { font-size: 20px; font-weight: 400; font-style: italic; margin-top: 7px; line-height: 26px; }
  .service-sub { list-style: none; font-weight: 400; font-size: 21px; line-height: 34px; margin-top: 4px; }
  .service-sub li { position: relative; padding-left: 22px; }
  .service-sub li::before { content: ""; position: absolute; left: 2px; top: 13px; width: 9px; height: 9px; border-radius: 50%; background: var(--white); }
  .service-emergency { margin-top: 12px; }

  .brand { left: 42px; top: 880px; width: 356px; display: flex; align-items: center; gap: 12px; }
  .brand-square { width: 34px; height: 34px; background: var(--brand-navy); flex: none; }
  .brand-name { font-size: 26px; font-weight: 700; line-height: 30px; color: var(--brand-navy); text-transform: uppercase; }
  .rule { left: 27px; top: 1002px; width: 372px; height: 1px; background: var(--ink-dark); }

  .contact { left: 35px; top: 1010px; color: var(--ink-grey); }
  .contact-lead { font-size: 21px; font-weight: 700; line-height: 28px; }
  .contact-phones { font-size: 32px; font-weight: 400; line-height: 40px; }
  .contact-phones span { font-size: 22px; font-weight: 700; }
  .contact-tail { font-size: 30px; font-weight: 700; line-height: 36px; }

  .promises { left: 432px; top: 916px; width: 384px; list-style: none; color: var(--ink-dark); font-size: 17px; line-height: 24px; }
  .promise { position: relative; padding-left: 24px; margin-bottom: 18px; }
  .promise::before { content: ""; position: absolute; left: 0; top: 8px; width: 9px; height: 9px; border-radius: 50%; background: var(--ink-dark); }
  .promise strong { font-weight: 700; }

  .footer { left: 0; top: 1124px; width: 846px; height: 52px; background: var(--brand-blue);
    display: flex; align-items: center; justify-content: space-between; padding: 0 30px 0 38px; color: var(--white); }
  .footer-web { font-size: 26px; font-weight: 700; }
  .footer-social { display: flex; align-items: center; gap: 18px; font-size: 21px; }
  .social-square { width: 32px; height: 32px; border: 2px solid var(--white); background: #3a6fb5; }
</style>
</head>
<body>
<div class="flyer">
  <div class="abs worker-photo" role="img" aria-label="Tradesman in a shirt and tool belt holding a yellow hard hat"></div>

  <svg class="abs band" width="846" height="1200" viewBox="0 0 846 1200" aria-hidden="true">
    <polygon points="0,224 846,328 846,904 0,796" fill="var(--brand-blue)"/>
  </svg>

  <header class="abs intro">
    <p class="intro-lead">Dunvarra Windows &amp; Home Improvements offer</p>
    <h1 class="intro-title">COMPLETE RENOVATIONS AND<br>IMPROVEMENT SERVICES</h1>
    <p class="intro-tail">from qualified and insured trade professionals.</p>
  </header>

  <div class="abs photo photo-sunroom" role="img" aria-label="Bungalow with a white uPVC sunroom and lawn"></div>
  <div class="abs photo photo-extension" role="img" aria-label="Stone clad extension with dark framed patio doors"></div>

  <div class="abs badge">
    <div class="badge-years"><strong>35</strong> Years</div>
    <div class="badge-label">Experience</div>
  </div>

  <ul class="abs services">
    <li class="service">A rated windows &nbsp;- double &amp; triple glazed</li>
    <li class="service">All types of doors, patio, French and UPVC</li>
    <li class="service">Specialists in Verandel Composite doors</li>
    <li class="service">Sunrooms &amp; Conservatories</li>
    <li class="service">Home improvements
      <p class="service-note">All types of home improvements</p>
      <ul class="service-sub">
        <li>Extension</li>
        <li>Renovations</li>
        <li>Roofing</li>
        <li>Fascia, Soffit &amp; Seamless Gutters</li>
      </ul>
    </li>
    <li class="service service-emergency">Emergency call out to replace<br>broken glass to secure homes.</li>
  </ul>

  <div class="abs brand">
    <span class="brand-square" aria-hidden="true"></span>
    <span class="brand-name">Dunvarra Windows<br>&amp; Home Improvements</span>
  </div>
  <div class="abs rule"></div>

  <div class="abs contact">
    <p class="contact-lead">call us on</p>
    <p class="contact-phones">06298173 <span>or</span> 0857304218</p>
    <p class="contact-tail">for a free quote.</p>
  </div>

  <ul class="abs promises">
    <li class="promise">We offer full project management from start to finish. Making sure all projects are finished to the <strong>highest standards</strong> with top quality market leading products with <strong>competitive prices.</strong></li>
    <li class="promise">With 35 years expertise in the business and a professional after sales service you can be sure <strong>customer satisfaction is guaranteed.</strong></li>
  </ul>

  <footer class="abs footer">
    <span class="footer-web">www.dunvarrawindows.com</span>
    <span class="footer-social">Like us on
      <span class="social-square" aria-hidden="true"></span>
      <span class="social-square" aria-hidden="true"></span>
    </span>
  </footer>
</div>
</body>
</html>
```